QTL Newsletter

QTL provides mortgage processing outsource services to Mortgage Lenders in Australia and New Zealand. The company employs approximately 300 staff based in offices in Sydney, Melbourne, Brisbane, Adelaide and Perth in Australia and Auckland, New Zealand.
The company acquired a similar and much larger business in 2012 which is being integrated into the one business.
The objectives of a newsletter are to:
- Support the development of the company culture
- Develp a sense of "one team"
- Provide a communication forum for management and staff
I am seeking design options for the newsletter. We will develop/include specific content which will likley evolve over time.
A copy of the company brand gudelines and logo is attached for reference. Our website is currently going through a redesign. Additional information can be provided on request.

Target Market(s)

The target market for the newsletter is staff. This is a diverse group in terms of locations, age, gender, occupations etc.

Industry/Entity Type

Communication

Requirements
Must have
• Information to be included in the newsletter should include:
- Business results (activity, volumes, performance to budget)
- Client news section (recent developments, client profiling etc)
- New initiatives (update on key projects and new business initiatives, initiatives roadmap)
- Office news (news section for each office including new employees, team profile of the month, report on social events)
- CEO report

```html
<!DOCTYPE html>
<html lang="en">
<head>
<meta charset="utf-8">
<title>QTL Newsletter – February 2013</title>
<link rel="stylesheet" href="https://fonts.googleapis.com/css2?family=Open+Sans:wght@300;400;600;700&display=swap">
<style>
  :root {
    --navy: #0b4c84;
    --teal: #2a8ab6;
    --brand: #1a4f8f;
    --ink: #333a40;
    --muted: #6b6f73;
    --rule: #c9ccd0;
    --frame: #cfd1d3;
    --white: #ffffff;
  }
  * { box-sizing: border-box; margin: 0; padding: 0; }
  html, body { width: 1200px; height: 3799px; overflow: hidden; background: var(--white); }
  body { font-family: "Open Sans", Arial, sans-serif; color: var(--ink); position: relative; }

  .abs { position: absolute; }

  /* Header */
  .view-link { left: 906px; top: 38px; font-size: 20px; color: var(--brand); }
  .top-bar { left: 80px; top: 70px; width: 1056px; height: 13px; background: var(--navy); }
  .brand-name { left: 150px; top: 128px; font-size: 92px; font-weight: 600; color: var(--brand); line-height: 1; }
  .social { left: 870px; top: 83px; display: flex; gap: 14px; }
  .social-item { width: 46px; display: flex; flex-direction: column; align-items: center; }
  .social-stem { width: 1px; height: 48px; background: var(--rule); }
  .social-dot { width: 46px; height: 46px; border: 2px solid #8a8d90; border-radius: 50%; display: block; }
  .issue-date { left: 872px; top: 212px; font-size: 24px; color: var(--ink); letter-spacing: 1px; }

  .banner { left: 80px; top: 278px; width: 1056px; height: 186px; background: var(--navy); border-bottom: 16px solid var(--frame); }
  .banner-art { left: 22px; top: 28px; width: 92px; height: 112px; background: linear-gradient(180deg, #e9eef3, #9fb4c7); border-radius: 4px; }
  .banner-text { left: 256px; top: 38px; color: var(--white); font-size: 29px; line-height: 1.55; }
  .banner-text small { font-size: 23px; }

  /* Shared */
  .section-title { font-size: 40px; font-weight: 300; color: var(--ink); line-height: 1; }
  .copy { font-size: 19px; line-height: 29px; color: var(--ink); }
  .photo { background: linear-gradient(135deg, #c9d3dc, #6f7f8f 60%, #3d4a57); }
  .photo-framed { border: 10px solid var(--frame); }
  .btn { display: inline-block; background: var(--white); color: var(--ink); border: 2px solid #b9bcbf; border-radius: 4px;
         font-size: 15px; font-weight: 600; padding: 10px 14px; line-height: 1; }

  /* News bands */
  .band { left: 80px; width: 1056px; color: var(--white); }
  .band-navy { background: var(--navy); }
  .band-teal { background: var(--teal); }
  .band .section-title { color: var(--white); position: absolute; left: 70px; top: 32px; }
  .news-item { position: absolute; width: 400px; }
  .news-title { font-size: 30px; font-weight: 300; line-height: 1; }
  .news-date { display: flex; align-items: center; gap: 14px; font-size: 18px; margin-top: 12px; }
  .news-text { font-size: 16.5px; font-weight: 700; line-height: 28px; margin-top: 14px; }
  .news-item .btn { position: absolute; }
  .divider { position: absolute; width: 0; border-left: 2px dotted rgba(255,255,255,.45); }
</style>
</head>
<body>

<header>
  <div class="abs view-link">Click here t view</div>
  <div class="abs top-bar"></div>
  <div class="abs brand-name">QTL</div>
  <div class="abs social" aria-label="Social links">
    <div class="social-item"><span class="social-stem"></span><span class="social-dot"></span></div>
    <div class="social-item"><span class="social-stem"></span><span class="social-dot"></span></div>
    <div class="social-item"><span class="social-stem"></span><span class="social-dot"></span></div>
  </div>
  <div class="abs issue-date">FEBRUARY 2013</div>

  <div class="abs banner">
    <div class="abs banner-art" role="img" aria-label="Illustration of an office building"></div>
    <div class="abs banner-text">PROVIDES MORTGAGE PROCESSING OUTSOURCE<br>SERVICES <small>to Mortgage Lenders in Australia and New Zealand</small></div>
  </div>
</header>

<section class="culture">
  <h2 class="abs section-title" style="left:150px; top:532px;">Company Culture</h2>
  <div class="abs photo photo-framed" style="left:150px; top:602px; width:432px; height:214px;" role="img" aria-label="Photo of colleagues talking in an office"></div>
  <p class="abs copy" style="left:627px; top:598px; width:510px;">Lorem Ipsum is simply dummy text of the printing and typesetting industry. Lorem Ipsum has been the industry's standard dummy text ever since the 1500s, when an unknown printer took a galley of type and scrambled it to make a type specimen book. It has survived not only five centuries, but also the leap into electronic typesetting, remaining essentially unchanged.</p>
</section>

<section class="activity">
  <h2 class="abs section-title" style="left:150px; top:968px;">Business activity</h2>
  <p class="abs copy" style="left:150px; top:1022px; width:440px;">Lorem Ipsum is simply dummy text of the printing and typesetting industry. Lorem Ipsum has been the industry's standard dummy text ever since the 1500s, when an unknown printer took a galley of type and scrambled it to make a type specimen book. It has survived not only five centuries, but also the leap into electronic typesetting, remaining essentially unchanged.</p>
  <div class="abs photo" style="left:618px; top:1034px; width:438px; height:294px; box-shadow:0 4px 10px rgba(0,0,0,.25);" role="img" aria-label="Photo of a business team working at a laptop"></div>
</section>

<section class="abs band band-navy" style="top:1398px; height:458px;">
  <h2 class="section-title">Office news</h2>
  <article class="news-item" style="left:144px; top:98px;">
    <h3 class="news-title">Office news1</h3>
    <div class="news-date"><svg width="20" height="20" viewBox="0 0 20 20" fill="none" stroke="#fff" stroke-width="2"><rect x="2" y="4" width="16" height="14"/><line x1="2" y1="8" x2="18" y2="8"/><line x1="6" y1="1" x2="6" y2="5"/><line x1="14" y1="1" x2="14" y2="5"/></svg>04.02.2013</div>
    <p class="news-text">Lorem Ipsum is simply dummy text of the printing and typesetting industry. Lorem Ipsum has been the industry's standard dummy text ever since the 1500s, when an unknown printer took a galley of type and scrambled it to make a type specimen book</p>
    <span class="btn" style="top:272px; left:0;">READ MORE</span>
  </article>
  <div class="divider" style="left:560px; top:110px; height:220px;"></div>
  <article class="news-item" style="left:605px; top:98px;">
    <h3 class="news-title">Office news2</h3>
    <div class="news-date"><svg width="20" height="20" viewBox="0 0 20 20" fill="none" stroke="#fff" stroke-width="2"><rect x="2" y="4" width="16" height="14"/><line x1="2" y1="8" x2="18" y2="8"/><line x1="6" y1="1" x2="6" y2="5"/><line x1="14" y1="1" x2="14" y2="5"/></svg>04.02.2013</div>
    <p class="news-text">Lorem Ipsum is simply dummy text of the printing and typesetting industry. Lorem Ipsum has been the industry's standard dummy text ever since the 1500s, when an unknown printer took a galley of type and scrambled it to make a type specimen book</p>
    <span class="btn" style="top:272px; left:0;">READ MORE</span>
  </article>
</section>

<section class="results">
  <div class="abs" style="left:150px; top:1898px; width:42px; height:42px; border-radius:50%; background:radial-gradient(circle at 35% 35%, #9fd0f5, #1f6fbf 70%);" role="img" aria-label="Globe icon"></div>
  <h2 class="abs section-title" style="left:218px; top:1896px;">Business results</h2>
  <p class="abs copy" style="left:218px; top:1955px; width:560px;">Lorem Ipsum is simply dummy text of the printing and type-setting industry. Lorem Ipsum has been the industry's standard dummy text ever since the 1500s, when an unknown printer took a galley of type and scrambled it to make a type specimen book.</p>
  <span class="abs btn" style="left:218px; top:2125px;">READ MORE</span>
  <div class="abs" style="left:830px; top:1958px; width:200px; height:190px; background:linear-gradient(180deg, #ece8f2 0%, #9cc76a 50%, #f0a04a 100%);" role="img" aria-label="Illustration of a results chart"></div>
</section>

<section class="abs band band-teal" style="top:2218px; height:454px;">
  <h2 class="section-title">Client news</h2>
  <article class="news-item" style="left:144px; top:98px;">
    <h3 class="news-title">Client news1</h3>
    <div class="news-date"><svg width="20" height="20" viewBox="0 0 20 20" fill="none" stroke="#fff" stroke-width="2"><rect x="2" y="4" width="16" height="14"/><line x1="2" y1="8" x2="18" y2="8"/><line x1="6" y1="1" x2="6" y2="5"/><line x1="14" y1="1" x2="14" y2="5"/></svg>04.02.2013</div>
    <p class="news-text">Lorem Ipsum is simply dummy text of the printing and typesetting industry. Lorem Ipsum has been the industry's standard dummy text ever since the 1500s, when an unknown printer took a galley of type and scrambled it to make a type specimen book</p>
    <span class="btn" style="top:272px; left:0;">READ MORE</span>
  </article>
  <div class="divider" style="left:560px; top:110px; height:220px;"></div>
  <article class="news-item" style="left:605px; top:98px;">
    <h3 class="news-title">Client news2</h3>
    <div class="news-date"><svg width="20" height="20" viewBox="0 0 20 20" fill="none" stroke="#fff" stroke-width="2"><rect x="2" y="4" width="16" height="14"/><line x1="2" y1="8" x2="18" y2="8"/><line x1="6" y1="1" x2="6" y2="5"/><line x1="14" y1="1" x2="14" y2="5"/></svg>04.02.2013</div>
    <p class="news-text">Lorem Ipsum is simply dummy text of the printing and typesetting industry. Lorem Ipsum has been the industry's standard dummy text ever since the 1500s, when an unknown printer took a galley of type and scrambled it to make a type specimen book</p>
    <span class="btn" style="top:272px; left:0;">READ MORE</span>
  </article>
</section>

<section class="initiatives">
  <h2 class="abs section-title" style="left:150px; top:2732px;">New initiatives</h2>
  <div class="abs photo photo-framed" style="left:150px; top:2800px; width:244px; height:176px;" role="img" aria-label="Photo of a team meeting around a laptop"></div>
  <p class="abs copy" style="left:432px; top:2800px; width:704px;">Lorem Ipsum is simply dummy text of the printing and typesetting industry. Lorem Ipsum has been the industry's standard dummy text ever since the 1500s, when an unknown printer took a galley of type and scrambled it to make a type specimen book.</p>
  <span class="abs btn" style="left:432px; top:2928px;">READ MORE</span>
  <div class="abs photo photo-framed" style="left:150px; top:3030px; width:244px; height:176px;" role="img" aria-label="Photo of a team meeting around a laptop"></div>
  <p class="abs copy" style="left:432px; top:3030px; width:704px;">Lorem Ipsum is simply dummy text of the printing and typesetting industry. Lorem Ipsum has been the industry's standard dummy text ever since the 1500s, when an unknown printer took a galley of type and scrambled it to make a type specimen book.</p>
  <span class="abs btn" style="left:432px; top:3158px;">READ MORE</span>
</section>

<section class="abs band band-navy" style="top:3270px; height:330px;">
  <h2 class="section-title" style="top:42px;">CEO report</h2>
  <p class="news-text abs" style="left:70px; top:96px; width:590px;">Lorem Ipsum is simply dummy text of the printing and typesetting industry. Lorem Ipsum has been the industry's standard dummy text ever since the 1500s, when an unknown printer took a galley of type and scrambled it to make a type specimen book</p>
  <span class="abs btn" style="left:70px; top:244px;">READ MORE</span>
  <div class="abs photo" style="left:704px; top:58px; width:234px; height:160px; border:5px solid var(--white);" role="img" aria-label="Photo of the CEO with colleagues"></div>
</section>

<footer>
  <div class="abs" style="left:528px; top:3638px; display:flex; gap:16px;">
    <span class="social-dot"></span><span class="social-dot"></span><span class="social-dot"></span>
  </div>
  <p class="abs" style="left:0; top:3700px; width:1200px; text-align:center; font-size:19px; line-height:26px; color:var(--muted);">You are receiving this email as a part of your company's program.<br>Copyright © 2012 QTL All rights reserved.</p>
</footer>

</body>
</html>
```